Brightfernrx website

We are a weight loss clinic and we need a website built. please look at these websites for content and style. Just need like 5 pages see samples. AI files of logo are not avail yet so use sample for place set

https://glowshiftstudio.com/
ortanvital.com
https://pinecrestclinicalbodybalance.com/
https://yourslimmingnook.com/
https://qrvskinstudio.com/treatments/weight-loss-injections/

Target Market(s)

Women

Industry/Entity Type

weight loss

Coding

Coded - Design and coding required

Number of Pages Required

5+ page

Requirements
Nice to have
• please make look like a medspa website

```html
<!DOCTYPE html>
<html lang="en">
<head>
<meta charset="utf-8">
<title>Brightfernrx — Stay Healthy</title>
<link href="https://fonts.googleapis.com/css2?family=Playfair+Display:wght@700;800&family=Poppins:ital,wght@0,400;0,500;0,600;1,400&display=swap" rel="stylesheet">
<style>
:root{
  --green:#7fb640;
  --green-dark:#6ea232;
  --blue:#1b95d3;
  --blue-dark:#1577b8;
  --ink:#2a2a2a;
  --text:#6b6b6b;
  --muted:#9a9a9a;
  --line:#e6e6e6;
  --footer:#333333;
  --footer-deep:#262626;
  --white:#ffffff;
}
*{box-sizing:border-box;margin:0;padding:0}
html,body{width:1200px;height:4862px;overflow:hidden;background:var(--white)}
body{font-family:"Poppins",sans-serif;color:var(--ink);position:relative}
.page{position:relative;width:1200px;height:4862px;overflow:hidden}
.abs{position:absolute}
.serif{font-family:"Playfair Display",serif;font-weight:800;text-transform:uppercase;color:var(--ink)}
a{color:inherit;text-decoration:none}

/* header */
.site-header{position:absolute;left:0;top:0;width:1200px;height:80px;background:var(--white);z-index:5}
.brand{position:absolute;left:89px;top:26px;display:flex;align-items:center;gap:8px;font-weight:600;font-size:17px;color:var(--green)}
.brand-dot{width:22px;height:22px;border-radius:50%;background:var(--green)}
.nav{position:absolute;top:33px;left:0;font-size:11.5px;font-weight:500;color:var(--ink);text-transform:uppercase}
.nav a{position:absolute;white-space:nowrap}
.nav .active{color:var(--blue)}
.btn-outline{position:absolute;left:998px;top:19px;width:112px;height:41px;border:2px solid var(--green);border-radius:21px;color:var(--green);font-size:11.5px;font-weight:600;display:flex;align-items:center;justify-content:center;text-transform:uppercase}

/* hero */
.hero-photo{left:0;top:80px;width:1200px;height:760px;background:linear-gradient(100deg,#6d7073 0%,#9a9ea1 40%,#c3c6c8 70%,#a9adb0 100%)}
.hero-eyebrow{left:89px;top:186px;color:var(--white);font-family:"Playfair Display",serif;font-size:18px;letter-spacing:.5px;display:flex;align-items:center;gap:14px;text-transform:uppercase;font-weight:700}
.hero-eyebrow::before{content:"";width:52px;height:2px;background:var(--white)}
.hero-title{left:89px;top:218px;color:var(--white);font-size:62px;line-height:58px;letter-spacing:.5px}
.hero-sub{left:89px;top:414px;color:var(--white);font-size:15.5px;line-height:23px;width:380px}
.btn-green{background:var(--green);color:var(--white);border-radius:22px;font-size:11px;font-weight:600;text-transform:uppercase;display:flex;align-items:center;justify-content:center}

.eyebrow{font-size:10.5px;font-weight:600;text-transform:uppercase;color:var(--ink);display:flex;align-items:center;gap:12px}
.eyebrow::before{content:"";width:36px;height:1px;background:#999}
.h2{font-size:33px;line-height:41px}
.body-copy{font-size:13.5px;line-height:23px;color:var(--text)}

/* approach */
.feature-icon{width:80px;height:80px;border-radius:50%;background:var(--blue);display:flex;align-items:center;justify-content:center}
.feature-title{font-size:17px;font-family:"Playfair Display",serif;font-weight:700;text-transform:uppercase;color:var(--ink)}
.feature-text{font-size:13px;line-height:21px;color:var(--text);width:300px}

/* specials */
.card{background:var(--white);border-radius:6px;box-shadow:0 10px 30px rgba(0,0,0,.10);overflow:hidden}
.card-img{width:100%;height:204px}
.card-body{padding:22px 24px}
.card-title{font-family:"Playfair Display",serif;font-weight:700;font-size:14.5px;line-height:20px;text-transform:uppercase;color:var(--ink);white-space:nowrap}
.card-text{font-size:12px;line-height:19px;color:var(--text);margin-top:10px}
.card-link{font-size:11px;font-weight:600;color:var(--muted);text-decoration:underline;margin-top:16px;display:block;text-transform:uppercase}

/* programs */
.prog{font-family:"Playfair Display",serif;font-weight:700;font-size:14px;text-transform:uppercase;color:var(--ink);white-space:nowrap}
.prog-line{height:1px;background:var(--line)}

/* testimonials */
.quote-mark{font-family:"Playfair Display",serif;font-size:110px;line-height:1;color:#e4e4e4}
.quote-text{font-size:14px;line-height:24px;font-style:italic;color:var(--text);width:390px}
.avatar{width:68px;height:68px;border-radius:50%;background:linear-gradient(135deg,#d9c9bd,#b9a596)}
.person{font-size:14px;font-weight:600;text-transform:uppercase;color:var(--ink)}
.year{font-size:12px;color:var(--muted)}
.arrow-btn{width:46px;height:46px;border-radius:50%;display:flex;align-items:center;justify-content:center}

/* blog */
.post-date{font-size:10.5px;color:var(--muted)}

/* cta */
.cta{left:136px;top:4129px;width:924px;height:183px;border-radius:92px;background:linear-gradient(90deg,var(--blue) 0%,#1f8fcf 55%,var(--blue-dark) 100%);z-index:3}
.cta-title{left:106px;top:40px;color:var(--white);font-size:31px;line-height:40px}
.cta-btn{position:absolute;left:645px;top:56px;width:183px;height:44px;border-radius:22px;background:var(--white);color:var(--ink);font-size:11.5px;font-weight:600;text-transform:uppercase;display:flex;align-items:center;justify-content:center}

/* footer */
.foot-h{font-family:"Playfair Display",serif;font-weight:700;font-size:17px;color:var(--white);text-transform:uppercase;white-space:nowrap}
.foot-list{list-style:none;font-size:12px;color:#e2e2e2}
.foot-list li{height:31px;display:flex;align-items:center;gap:8px}
.foot-list li::before{content:"›";color:#e2e2e2;font-size:14px}
.contact-item{font-size:12px;line-height:18px;color:#e2e2e2;display:flex;gap:10px}
.news-input{left:813px;top:4617px;width:259px;height:42px;border-radius:21px;background:var(--white);display:flex;align-items:center;padding:0 18px;font-size:11.5px;color:var(--muted);gap:8px}
.copyright{left:0;top:4804px;width:1200px;height:58px;background:var(--footer-deep);color:var(--white);font-size:11.5px;font-weight:500;display:flex;align-items:center;justify-content:center}
.to-top{left:1129px;top:4778px;width:44px;height:44px;border-radius:50%;background:var(--green);display:flex;align-items:center;justify-content:center}
</style>
</head>
<body>
<div class="page">

<header class="site-header">
  <a class="brand" href="#"><span class="brand-dot"></span>Brightfernrx</a>
  <nav class="nav">
    <a class="active" style="left:434px" href="#">Home</a>
    <a style="left:500px" href="#">About Us</a>
    <a style="left:590px" href="#">Specials</a>
    <a style="left:676px" href="#">Our Approach</a>
    <a style="left:802px" href="#">Results</a>
    <a style="left:880px" href="#">Contact Us</a>
  </nav>
  <a class="btn-outline" href="#">Get Started</a>
</header>

<!-- hero -->
<section class="hero">
  <div class="abs hero-photo" role="img" aria-label="Photo of a woman jogging outdoors with earphones"></div>
  <svg class="abs" style="left:0;top:560px" width="1200" height="290" viewBox="0 560 1200 290">
    <path d="M0 628 C140 596 250 640 420 724 C600 806 800 748 1000 742 C1100 740 1170 790 1200 826 L1200 850 L0 850Z" fill="#e9eaeb"/>
    <path d="M0 652 C140 618 250 662 420 742 C600 820 800 764 1000 760 C1100 758 1170 806 1200 840 L1200 850 L0 850Z" fill="#ffffff"/>
  </svg>
  <div class="abs hero-eyebrow">Welcome to</div>
  <h1 class="abs serif hero-title" style="color:#fff">Stay Healthy<br>Even If You Say<br>At Home</h1>
  <p class="abs hero-sub">Specializes provide non medical &amp; medical assistance to elderly people.</p>
  <a class="abs btn-green" style="left:89px;top:483px;width:166px;height:40px" href="#">Start Scheduling</a>
</section>

<!-- about -->
<section class="about">
  <div class="abs" style="left:136px;top:980px;width:400px;height:350px;border-radius:48% 52% 46% 54% / 40% 44% 56% 60%;background:#7bbdb7"></div>
  <div class="abs" role="img" aria-label="Photo of a young woman holding a bathroom scale and a measuring tape" style="left:200px;top:792px;width:404px;height:538px;border-radius:45% 55% 50% 50% / 30% 30% 70% 70%;background:linear-gradient(180deg,#e7ddd2 0%,#c9beb4 60%,#a9c9c5 100%)"></div>
  <div class="abs eyebrow" style="left:676px;top:933px">About Us</div>
  <h2 class="abs serif h2" style="left:676px;top:958px;width:420px">Want It Online Or<br>Video You Can Feel It</h2>
  <p class="abs body-copy" style="left:676px;top:1044px;width:392px">Aenean sollicitudin, lorem quis bibendum auctor, nisi elit consequat ipsum, nec sagittis sem nibh id elit duis sed odio sit amet nibh vulputate cursus a sit amet mauris. Morbi accumsan ipsum velit. Nam nec tellus a odio tincidunt auctor a ornare odio. Sed non &nbsp;mauris vitae erat consequat auctor eu in elit class aptent taciti sociosqu ad litora...</p>
  <a class="abs btn-green" style="left:674px;top:1227px;width:128px;height:40px" href="#">Learn More</a>
</section>

<!-- specials green wave (behind) -->
<svg class="abs" style="left:0;top:1780px" width="1200" height="720" viewBox="0 1780 1200 720">
  <path d="M0 1820 C120 1960 300 2064 560 2046 C800 2028 1000 1904 1200 1884 L1200 2300 C1150 2420 1000 2480 600 2480 C250 2480 60 2410 0 2250Z" fill="#d4d6d8"/>
  <path d="M0 1820 C120 1960 300 2050 560 2032 C800 2014 1000 1892 1200 1870 L1200 2240 C1150 2380 1000 2450 600 2455 C250 2455 60 2390 0 2230Z" fill="var(--green)"/>
</svg>

<!-- approach -->
<section class="approach">
  <div class="abs" style="left:566px;top:1380px;width:660px;height:582px;border-radius:50% 40% 45% 50% / 55% 40% 60% 45%;background:#d7d9db"></div>
  <div class="abs" role="img" aria-label="Photo of a smiling woman flexing her arm in loose trousers" style="left:626px;top:1378px;width:600px;height:572px;border-radius:46% 34% 40% 46% / 50% 36% 56% 44%;background:linear-gradient(160deg,#f2f2f2 0%,#e3e1df 50%,#cfd2d4 100%)"></div>
  <div class="abs eyebrow" style="left:90px;top:1449px">Our Approach</div>
  <h2 class="abs serif h2" style="left:90px;top:1473px;width:460px">Featured Program<br>Of The Month</h2>

  <div class="abs feature-icon" style="left:90px;top:1579px">
    <svg width="38" height="38" viewBox="0 0 24 24" fill="none" stroke="#fff" stroke-width="1.5"><rect x="5" y="4" width="14" height="17" rx="1"/><path d="M9 4V2h6v2M8 9h8M8 13h8M8 17h5"/></svg>
  </div>
  <div class="abs feature-title" style="left:185px;top:1589px">Weightloss Plans</div>
  <p class="abs feature-text" style="left:185px;top:1619px">Aenean sollicitudin, lorem quis bibendum auctor nisi elit consequat ipsum...</p>

  <div class="abs feature-icon" style="left:90px;top:1679px">
    <svg width="38" height="38" viewBox="0 0 24 24" fill="none" stroke="#fff" stroke-width="1.5"><rect x="3" y="8" width="18" height="11" rx="2"/><path d="M12 10v7M8.5 13.5h7M9 8V5h6v3"/></svg>
  </div>
  <div class="abs feature-title" style="left:185px;top:1689px">Medications</div>
  <p class="abs feature-text" style="left:185px;top:1719px">Aenean sollicitudin, lorem quis bibendum auctor nisi elit consequat ipsum...</p>

  <div class="abs feature-icon" style="left:90px;top:1777px">
    <svg width="38" height="38" viewBox="0 0 24 24" fill="none" stroke="#fff" stroke-width="1.5"><path d="M18 2l4 4M20 4l-9 9M15 5l4 4M13 7l4 4-8 8H5v-4z"/><path d="M5 19l-3 3"/></svg>
  </div>
  <div class="abs feature-title" style="left:185px;top:1786px">Injections</div>
  <p class="abs feature-text" style="left:185px;top:1816px">Aenean sollicitudin, lorem quis bibendum auctor nisi elit consequat ipsum...</p>
</section>

<!-- specials -->
<section class="specials">
  <h2 class="abs serif" style="left:0;top:2094px;width:1200px;text-align:center;color:#fff;font-size:32px">Specials</h2>
  <p class="abs" style="left:0;top:2142px;width:1200px;text-align:center;color:#fff;font-size:14px">Specializes provide non medical &amp; medical assistance to elderly people.</p>

  <article class="abs card" style="left:104px;top:2196px;width:239px;height:367px">
    <div class="card-img" role="img" aria-label="Photo of a woman holding out oversized jeans" style="background:linear-gradient(180deg,#9fc6d6,#6e9fb4)"></div>
    <div class="card-body"><div class="card-title">Monitoring of<br>Medication</div><p class="card-text">Aenean sollicit lorem auctor elit consequat ipsum...</p><a class="card-link" href="#">Learn More</a></div>
  </article>
  <article class="abs card" style="left:355px;top:2196px;width:239px;height:367px">
    <div class="card-img" role="img" aria-label="Photo of women doing a step aerobics class" style="background:linear-gradient(180deg,#e9e3dc,#c7b9ad)"></div>
    <div class="card-body"><div class="card-title">Personal Care<br>Services</div><p class="card-text">Aenean sollicit lorem auctor elit consequat ipsum...</p><a class="card-link" href="#">Learn More</a></div>
  </article>
  <article class="abs card" style="left:606px;top:2196px;width:239px;height:367px">
    <div class="card-img" role="img" aria-label="Photo of a person holding a bathroom scale" style="background:linear-gradient(180deg,#8fa9b5,#4f6e7c)"></div>
    <div class="card-body"><div class="card-title">Weekend and<br>Holiday Care</div><p class="card-text">Aenean sollicit lorem auctor elit consequat ipsum...</p><a class="card-link" href="#">Learn More</a></div>
  </article>
  <article class="abs card" style="left:859px;top:2196px;width:239px;height:367px">
    <div class="card-img" role="img" aria-label="Photo of a woman lunging with dumbbells" style="background:linear-gradient(180deg,#e4e4e4,#b9b9b9)"></div>
    <div class="card-body"><div class="card-title">Social and Recreational<br>Activities</div><p class="card-text">Aenean sollicit lorem auctor elit consequat ipsum...</p><a class="card-link" href="#">Learn More</a></div>
  </article>
</section>

<!-- programs -->
<section class="programs">
  <h2 class="abs serif h2" style="left:0;top:2636px;width:1200px;text-align:center">Program Classes That<br>You Can Take</h2>
  <svg class="abs" style="left:420px;top:2752px" width="260" height="260" viewBox="0 0 260 260"><circle cx="130" cy="130" r="108" fill="none" stroke="var(--green)" stroke-width="40"/></svg>
  <div class="abs" role="img" aria-label="Photo of a woman sprinting in athletic wear" style="left:470px;top:2740px;width:300px;height:330px;border-radius:45% 55% 40% 60% / 40% 45% 55% 60%;background:linear-gradient(150deg,rgba(120,120,125,.55),rgba(60,70,80,.7))"></div>

  <div class="abs prog" style="left:90px;top:2807px;width:231px;text-align:right">Zumba Exercise</div>
  <div class="abs prog" style="left:90px;top:2870px;width:231px;text-align:right">Aeroic Gymnastics</div>
  <div class="abs prog" style="left:90px;top:2932px;width:231px;text-align:right">Cardio Exercise</div>
  <div class="abs prog-line" style="left:90px;top:2850px;width:297px"></div>
  <div class="abs prog-line" style="left:90px;top:2912px;width:297px"></div>
  <div class="abs prog-line" style="left:90px;top:2975px;width:297px"></div>
  <svg class="abs" style="left:350px;top:2802px" width="30" height="30" viewBox="0 0 24 24" fill="none" stroke="var(--blue)" stroke-width="1.4"><circle cx="12" cy="5" r="3"/><path d="M5 22v-6a7 7 0 0 1 14 0v6"/></svg>
  <svg class="abs" style="left:350px;top:2865px" width="30" height="30" viewBox="0 0 24 24" fill="none" stroke="var(--blue)" stroke-width="1.4"><circle cx="7" cy="16" r="5"/><circle cx="17" cy="16" r="5"/><circle cx="12" cy="4" r="2"/><path d="M12 6v6"/></svg>
  <svg class="abs" style="left:350px;top:2927px" width="30" height="30" viewBox="0 0 24 24" fill="none" stroke="var(--blue)" stroke-width="1.4"><circle cx="6" cy="18" r="4"/><circle cx="18" cy="18" r="4"/><path d="M6 18l5-8h5l2 8M14 4h3"/></svg>

  <svg class="abs" style="left:738px;top:2802px" width="30" height="30" viewBox="0 0 24 24" fill="none" stroke="var(--blue)" stroke-width="1.4"><rect x="4" y="3" width="16" height="6" rx="2"/><path d="M12 9v4M8 22l4-9 4 9"/></svg>
  <svg class="abs" style="left:738px;top:2865px" width="30" height="30" viewBox="0 0 24 24" fill="none" stroke="var(--blue)" stroke-width="1.4"><path d="M4 20c0-6 3-9 7-9l2-5h3l-1 5c3 1 5 4 5 9z"/></svg>
  <svg class="abs" style="left:738px;top:2927px" width="30" height="30" viewBox="0 0 24 24" fill="none" stroke="var(--blue)" stroke-width="1.4"><circle cx="12" cy="4" r="2.5"/><path d="M12 7v8M7 10h10M9 22l3-7 3 7"/></svg>
  <div class="abs prog" style="left:794px;top:2807px">Whole Body Fat Loss</div>
  <div class="abs prog" style="left:794px;top:2870px">Building Muscle Mass</div>
  <div class="abs prog" style="left:794px;top:2932px">Level 2 Muscle Gain</div>
  <div class="abs prog-line" style="left:736px;top:2850px;width:298px"></div>
  <div class="abs prog-line" style="left:736px;top:2912px;width:298px"></div>
  <div class="abs prog-line" style="left:736px;top:2975px;width:298px"></div>
</section>

<!-- testimonials -->
<section class="testimonials">
  <h2 class="abs serif h2" style="left:0;top:3134px;width:1200px;text-align:center">What Our Client Say</h2>
  <div class="abs arrow-btn" style="left:1009px;top:3132px;background:var(--green)"><svg width="16" height="16" viewBox="0 0 24 24" fill="none" stroke="#fff" stroke-width="2"><path d="M20 12H4M10 6l-6 6 6 6"/></svg></div>
  <div class="abs arrow-btn" style="left:1064px;top:3132px;background:var(--blue)"><svg width="16" height="16" viewBox="0 0 24 24" fill="none" stroke="#fff" stroke-width="2"><path d="M4 12h16M14 6l6 6-6 6"/></svg></div>

  <div class="abs quote-mark" style="left:250px;top:3196px">“</div>
  <p class="abs quote-text" style="left:90px;top:3256px">Very happy with Maple Lane decorators. Noah and Priya did a great job with good communication and attention to detail. Definitely recommend... good value for money!</p>
  <div class="abs avatar" role="img" aria-label="Client portrait" style="left:90px;top:3376px"></div>
  <div class="abs person" style="left:174px;top:3388px">Owen Hartley</div>
  <div class="abs year" style="left:174px;top:3410px">(2020)</div>

  <div class="abs quote-mark" style="left:706px;top:3196px">“</div>
  <p class="abs quote-text" style="left:545px;top:3256px">Very happy with Maple Lane decorators. Noah and Priya did a great job with good communication and attention to detail. Definitely recommend... good value for money!</p>
  <div class="abs avatar" role="img" aria-label="Client portrait" style="left:545px;top:3376px"></div>
  <div class="abs person" style="left:629px;top:3388px">Ravi Mendes</div>
  <div class="abs year" style="left:629px;top:3410px">(2020)</div>

  <div class="abs quote-mark" style="left:1160px;top:3196px">“</div>
  <p class="abs quote-text" style="left:998px;top:3256px">Very happy with Maple Lane decorators. Noah and Priya did a great job with good communication and attention to detail. Definitely recommend... good value for money!</p>
  <div class="abs avatar" role="img" aria-label="Client portrait" style="left:998px;top:3376px;background:linear-gradient(135deg,#8a6a55,#5a4336)"></div>
  <div class="abs person" style="left:1082px;top:3388px">Tessa Quinlan</div>
  <div class="abs year" style="left:1082px;top:3410px">(2020)</div>

  <div class="abs" style="left:90px;top:3510px;width:1020px;height:1px;background:var(--line)"></div>
</section>

<!-- blog -->
<section class="blog">
  <h2 class="abs serif h2" style="left:0;top:3582px;width:1200px;text-align:center">Latest Blog</h2>
  <article class="abs card" style="left:172px;top:3650px;width:273px;height:366px">
    <div class="card-img" role="img" aria-label="Photo of a woman comparing before and after weight loss" style="height:203px;background:linear-gradient(90deg,#cfc8c0,#e9e6e2,#cfc8c0)"></div>
    <div class="card-body"><div class="post-date">25-02-2022</div><div class="card-title" style="margin-top:10px">Some Event Heading<br>Goes Here</div><p class="card-text">Aenean sollicitudin lorem bibendum auctor nisi elit consequat ipsum...</p></div>
  </article>
  <article class="abs card" style="left:464px;top:3650px;width:274px;height:366px">
    <div class="card-img" role="img" aria-label="Photo of a slim waist in loose jeans" style="height:203px;background:linear-gradient(180deg,#d8cfc6,#a99d92)"></div>
    <div class="card-body"><div class="post-date">25-02-2022</div><div class="card-title" style="margin-top:10px">Some Event Heading<br>Goes Here</div><p class="card-text">Aenean sollicitudin lorem bibendum auctor nisi elit consequat ipsum...</p></div>
  </article>
  <article class="abs card" style="left:757px;top:3650px;width:273px;height:366px">
    <div class="card-img" role="img" aria-label="Photo of two women working out with weights" style="height:203px;background:linear-gradient(180deg,#d9b7a3,#3f78b8)"></div>
    <div class="card-body"><div class="post-date">25-02-2022</div><div class="card-title" style="margin-top:10px">Some Event Heading<br>Goes Here</div><p class="card-text">Aenean sollicitudin lorem bibendum auctor nisi elit consequat ipsum...</p></div>
  </article>
</section>

<!-- footer background -->
<svg class="abs" style="left:0;top:4280px" width="1200" height="582" viewBox="0 4280 1200 582">
  <path d="M0 4316 C200 4372 400 4448 620 4410 C850 4370 1000 4300 1200 4290 L1200 4862 L0 4862Z" fill="var(--footer)"/>
</svg>

<!-- cta -->
<section class="abs cta">
  <h2 class="abs serif cta-title" style="color:#fff">Call And Schedule Your<br>Appointment Today!</h2>
  <a class="cta-btn" href="#">Request a Callback</a>
</section>

<!-- footer -->
<footer>
  <div class="abs foot-h" style="left:157px;top:4509px">Information</div>
  <ul class="abs foot-list" style="left:157px;top:4552px">
    <li>Terms &amp; Condition</li><li>Privacy Policy</li><li>Site Map</li><li>FAQ's</li><li>Reviews</li>
  </ul>
  <div class="abs foot-h" style="left:379px;top:4509px">Quick Links</div>
  <ul class="abs foot-list" style="left:379px;top:4552px">
    <li>Home</li><li>About Us</li><li>Specials</li><li>Our Approach</li><li>Results</li><li>Contact Us</li>
  </ul>
  <div class="abs foot-h" style="left:564px;top:4509px">Contact Info</div>
  <div class="abs contact-item" style="left:564px;top:4556px">
    <svg width="14" height="14" viewBox="0 0 24 24" fill="var(--green)"><path d="M2 5h20v14H2z"/><path d="M2 5l10 8 10-8" stroke="#333" stroke-width="2" fill="none"/></svg>
    <div>Email:<br>hello@brightfernrx.com.au</div>
  </div>
  <div class="abs contact-item" style="left:564px;top:4610px">
    <svg width="14" height="14" viewBox="0 0 24 24" fill="var(--green)"><path d="M6 2l4 4-2 3a12 12 0 0 0 7 7l3-2 4 4-3 4C10 22 2 14 2 5z"/></svg>
    <div>Phone:<br>+08 321 654 0987</div>
  </div>
  <div class="abs contact-item" style="left:564px;top:4664px">
    <svg width="14" height="14" viewBox="0 0 24 24" fill="var(--green)"><path d="M12 2a7 7 0 0 0-7 7c0 5 7 13 7 13s7-8 7-13a7 7 0 0 0-7-7zm0 10a3 3 0 1 1 0-6 3 3 0 0 1 0 6z"/></svg>
    <div>Location:<br>Some address line here<br>United Kingdom FX12 9QB</div>
  </div>
  <div class="abs foot-h" style="left:813px;top:4509px">Newsletter</div>
  <p class="abs" style="left:813px;top:4556px;width:230px;font-size:12px;line-height:18px;color:#e2e2e2">Subscribe to our email address to get the latest news.</p>
  <div class="abs news-input">
    <svg width="12" height="12" viewBox="0 0 24 24" fill="none" stroke="#aaa" stroke-width="2"><rect x="2" y="5" width="20" height="14"/><path d="M2 5l10 8 10-8"/></svg>
    <span style="flex:1">Enter your email...</span>
    <svg width="16" height="16" viewBox="0 0 24 24" fill="var(--green)"><path d="M2 12L22 3l-7 19-3-8z"/></svg>
  </div>
  <div class="abs copyright">© Copyright 2023, All Rights Reserved</div>
  <div class="abs to-top"><svg width="16" height="16" viewBox="0 0 24 24" fill="none" stroke="#fff" stroke-width="2"><path d="M12 20V4M6 10l6-6 6 6"/></svg></div>
</footer>

</div>
</body>
</html>
```